" Nossa empresa oferece diversos tipos de soluçoes na área de Gestao de Ativos para empresas do Setor Elétrico Brasileiro. Somos uma empresa Jovem com grandes ambiçoes. Apesar de pequenos, já temos na nossa carteira grandes empresas do setor e nosso objetivo agora é ampliar os serviços nas empresas em que já atuamos e conquistar novos clientes "

```html
<!DOCTYPE html>
<html lang="pt-BR">
<head>
<meta charset="utf-8">
<title>Voltra – Gestão de Ativos</title>
<link href="https://fonts.googleapis.com/css2?family=Open+Sans:wght@400;600;700&family=Oswald:wght@400;500;600&display=swap" rel="stylesheet">
<style>
:root{
  --bg:#ffffff;
  --nav:#1c2633;
  --blue:#2b6fc6;
  --blue-deep:#1b54a3;
  --blue-light:#5d9de0;
  --dark:#3b3d40;
  --ink:#4a4f57;
  --muted:#8a9099;
  --white:#ffffff;
}
*{box-sizing:border-box;margin:0;padding:0}
html,body{width:1200px;height:1200px;overflow:hidden;background:var(--bg);font-family:"Open Sans",sans-serif;color:var(--ink)}
.page{position:absolute;left:348px;top:0;width:504px;height:1200px;background:var(--white);overflow:hidden}
.brand{font-family:"Open Sans",sans-serif;font-weight:700;color:var(--white);display:flex;align-items:center;gap:5px}
.brand-dot{width:10px;height:10px;border-radius:50%;background:var(--blue-light)}

/* nav */
.nav{position:absolute;top:0;left:0;right:0;height:34px;background:var(--nav);display:flex;align-items:center;padding:0 14px}
.nav .brand{font-size:15px}
.menu{display:flex;gap:12px;margin-left:44px;font-size:6px;font-weight:600;color:#c9d2dd;text-transform:uppercase}
.menu .active{color:var(--white);border-bottom:2px solid var(--blue-light);padding-bottom:2px}
.nav-phone{margin-left:auto;font-size:8px;color:var(--white);font-weight:600;display:flex;align-items:center;gap:4px}

/* hero */
.hero{position:absolute;top:34px;left:0;right:0;height:250px;
  background:
    linear-gradient(180deg,rgba(255,255,255,0) 55%,rgba(28,38,51,.55) 100%),
    radial-gradient(ellipse 60px 110px at 80px 190px,#2c3a4d 0%,rgba(44,58,77,0) 100%),
    radial-gradient(ellipse 260px 120px at 320px 220px,#3b4f6b 0%,rgba(59,79,107,0) 100%),
    linear-gradient(100deg,#dfe7ef 0%,#a9c0d8 35%,#6f8fb5 70%,#9fb7d2 100%)}
.hero-tags{position:absolute;left:30px;top:142px;display:flex;flex-direction:column;gap:6px}
.hero-tag{font-family:"Oswald",sans-serif;font-weight:500;color:var(--white);background:rgba(20,30,45,.82);padding:4px 8px;font-size:13px;letter-spacing:.5px;align-self:flex-start}
.hero-arrows{position:absolute;left:30px;top:212px;display:flex;gap:8px;color:var(--white);font-size:12px;font-weight:700}
.hero-dots{position:absolute;left:50%;bottom:8px;display:flex;gap:4px;transform:translateX(-50%)}
.hero-dots span{width:4px;height:4px;border-radius:50%;background:rgba(255,255,255,.6)}
.hero-dots span:first-child{background:var(--white)}

/* about */
.about{position:absolute;top:284px;left:0;right:0;height:150px;background:var(--white)}
.cycle{position:absolute;left:18px;top:-22px;width:150px;height:150px}
.about-text{position:absolute;left:196px;top:10px;width:170px}
.section-title{font-family:"Oswald",sans-serif;font-weight:500;font-size:13px;color:var(--blue);display:flex;align-items:center;gap:5px;margin-bottom:6px}
.title-icon{width:12px;height:12px;border-radius:50%;background:var(--blue);display:inline-block}
.about-text p{font-size:5.6px;line-height:1.55;color:var(--ink)}
.btn{display:inline-block;margin-top:8px;background:var(--blue);color:var(--white);font-size:5.5px;font-weight:700;padding:4px 8px;text-transform:uppercase}
.about-photo{position:absolute;right:10px;top:0;width:118px;height:126px;
  background:
    radial-gradient(ellipse 40px 60px at 80px 110px,#2b3644 0%,rgba(43,54,68,0) 100%),
    linear-gradient(160deg,#f1f3f5 0%,#d4dbe3 55%,#9aa8b8 100%)}

/* services */
.services{position:absolute;top:434px;left:0;right:0;height:192px;background:linear-gradient(180deg,var(--blue-light),var(--blue))}
.services .section-title{color:var(--white);justify-content:center;margin-top:10px}
.services .title-icon{background:var(--white)}
.service-grid{display:grid;grid-template-columns:repeat(3,1fr);gap:22px 16px;padding:20px 46px 0}
.service{display:flex;gap:6px}
.service svg{flex:none}
.service h3{font-size:5.5px;font-weight:700;color:var(--white);text-transform:uppercase;margin-bottom:2px}
.service p{font-size:5px;line-height:1.5;color:#e3eefb}

/* team */
.team{position:absolute;top:626px;left:0;right:0;height:198px;background:var(--dark)}
.team .section-title{color:var(--white);justify-content:center;margin-top:14px}
.team .title-icon{background:var(--blue-light);border-radius:2px}
.team-rule{width:300px;height:1px;background:#5b5e63;margin:-2px auto 14px}
.team-grid{display:flex;gap:8px;justify-content:center}
.member{width:110px}
.member-photo{height:94px;border:3px solid var(--white);
  background:
    radial-gradient(ellipse 34px 40px at 52px 94px,#2a3340 0%,rgba(42,51,64,0) 100%),
    linear-gradient(170deg,#f3f5f7 0%,#cfd7e0 60%,#93a2b3 100%)}
.member-name{font-size:5.5px;color:#cfd4da;margin-top:5px;white-space:nowrap}
.member-name b{color:var(--blue-light)}

/* testimonial */
.testimonial{position:absolute;top:824px;left:0;right:0;height:184px;background:linear-gradient(180deg,var(--blue-deep),var(--blue))}
.testimonial .section-title{color:var(--white);justify-content:center;margin-top:12px}
.testimonial .title-icon{background:var(--white)}
.building{position:absolute;right:18px;top:24px;width:150px;height:160px;
  background:
    linear-gradient(90deg,rgba(255,255,255,.25) 0%,rgba(255,255,255,0) 40%,rgba(10,40,90,.25) 100%),
    linear-gradient(180deg,#c7def5 0%,#6ea2db 45%,#2f68b5 100%)}
.quote{position:absolute;left:40px;top:52px;width:290px;color:var(--white)}
.quote-mark{font-family:"Oswald",sans-serif;font-size:32px;line-height:1}
.quote p{font-size:7.5px;line-height:1.55;margin-top:2px}
.author{display:flex;align-items:center;gap:6px;margin:10px 0 0 160px}
.author-photo{width:20px;height:20px;border-radius:50%;background:linear-gradient(160deg,#e6d6c8,#8a7a6c)}
.author-name{font-size:6px;font-weight:700}
.author-role{font-size:5px;color:#dbe7f6}

/* clients */
.clients{position:absolute;top:1008px;left:0;right:0;height:48px;display:flex;justify-content:center;align-items:center;gap:10px;border-bottom:1px solid #e4e7eb}
.client{width:52px;height:22px;background:#e6eaef;border:1px solid #cfd5dc}

/* footer */
.footer{position:absolute;top:1058px;left:0;right:0;height:106px;display:grid;grid-template-columns:1fr 1fr 1fr 1fr;gap:10px;padding:12px 22px}
.footer h4{font-size:6px;font-weight:700;color:var(--blue);text-transform:uppercase;margin-bottom:4px}
.footer p{font-size:5px;line-height:1.55;color:var(--muted)}
.contact-row{display:flex;gap:4px;margin-bottom:6px}
.field{height:9px;border:1px solid #d5dae0;margin-bottom:4px;font-size:4.5px;color:var(--muted);padding:1px 3px}
.field.tall{height:22px}
.send{background:var(--blue);color:var(--white);font-size:5px;font-weight:700;padding:2px 6px;display:inline-block;float:right}
.map{height:70px;background:linear-gradient(135deg,#eef0ea 0%,#dfe3dc 50%,#cfd6de 100%);border:1px solid #d5dae0}

/* bottom */
.bottom{position:absolute;top:1164px;left:0;right:0;height:36px;background:var(--blue-deep);display:flex;align-items:center;padding:0 22px}
.bottom .brand{font-size:14px}
.bottom .menu{margin-left:auto;color:#dbe7f6}
</style>
</head>
<body>
<div class="page">

  <header class="nav">
    <div class="brand"><span class="brand-dot"></span>Voltra</div>
    <nav class="menu">
      <span class="active">Página inicial</span><span>Quem somos</span><span>O que fazemos</span><span>Parceiros</span><span>Atendimento</span>
    </nav>
    <div class="nav-phone">
      <svg width="8" height="8" viewBox="0 0 24 24"><path fill="#fff" d="M6.6 10.8a15 15 0 0 0 6.6 6.6l2.2-2.2c.3-.3.7-.4 1-.2 1.1.4 2.3.6 3.6.6.6 0 1 .4 1 1V20c0 .6-.4 1-1 1A17 17 0 0 1 3 4c0-.6.4-1 1-1h3.5c.6 0 1 .4 1 1 0 1.3.2 2.5.6 3.6.1.3 0 .7-.2 1z"/></svg>
      (11) 4000-1234
    </div>
  </header>

  <section class="hero" role="img" aria-label="Foto de executivos em escritório corporativo">
    <div class="hero-tags">
      <span class="hero-tag">SOLUÇÕES EM GESTÃO DE ATIVOS</span>
      <span class="hero-tag">PARA EMPRESAS DO SETOR ELÉTRICO</span>
    </div>
    <div class="hero-arrows"><span>‹</span><span>›</span></div>
    <div class="hero-dots"><span></span><span></span><span></span><span></span></div>
  </section>

  <section class="about">
    <svg class="cycle" viewBox="0 0 150 150">
      <defs>
        <path id="ring-top" d="M21 75 A54 54 0 0 1 129 75"/>
        <path id="ring-bottom" d="M21 75 A54 54 0 0 0 129 75"/>
      </defs>
      <circle cx="75" cy="75" r="73" fill="#fff"/>
      <circle cx="75" cy="75" r="68" fill="none" stroke="#cfd8e3" stroke-width="3"/>
      <circle cx="75" cy="75" r="54" fill="none" stroke="#1c2f4d" stroke-width="20"/>
      <path d="M75 21 A54 54 0 0 1 129 75" fill="none" stroke="#2b6fc6" stroke-width="20"/>
      <path d="M75 129 A54 54 0 0 1 21 75" fill="none" stroke="#2b6fc6" stroke-width="20"/>
      <circle cx="75" cy="75" r="42" fill="#fff"/>
      <circle cx="57" cy="75" r="4" fill="#2b6fc6"/>
      <text x="65" y="78.5" font-family="Open Sans, sans-serif" font-weight="700" font-size="10" fill="#1c2f4d">Voltra</text>
      <g font-family="Open Sans, sans-serif" font-size="5.5" fill="#fff" font-weight="600" text-anchor="middle" dominant-baseline="middle">
        <text><textPath href="#ring-top" startOffset="25%">Planejamento</textPath></text>
        <text><textPath href="#ring-top" startOffset="75%">Execução</textPath></text>
        <text><textPath href="#ring-bottom" startOffset="75%">Controle</textPath></text>
        <text><textPath href="#ring-bottom" startOffset="25%">Melhoria</textPath></text>
      </g>
    </svg>
    <div class="about-text">
      <h2 class="section-title"><span class="title-icon"></span>QUEM SOMOS?</h2>
      <p>Somos uma empresa jovem de gestão de ativos para o setor elétrico brasileiro. Apesar de pequenos, já atendemos grandes empresas do setor e queremos ampliar nossos serviços e conquistar novos clientes com qualidade e compromisso.</p>
      <span class="btn">Saiba mais ›</span>
    </div>
    <div class="about-photo" role="img" aria-label="Foto de profissional em reunião de trabalho"></div>
  </section>

  <section class="services">
    <h2 class="section-title"><span class="title-icon"></span>O QUE FAZEMOS?</h2>
    <div class="service-grid">
      <div class="service"><svg width="14" height="14" viewBox="0 0 24 24"><circle cx="12" cy="12" r="4" fill="none" stroke="#fff" stroke-width="2"/><path d="M12 2v4M12 18v4M2 12h4M18 12h4M5 5l3 3M16 16l3 3M5 19l3-3M16 8l3-3" stroke="#fff" stroke-width="2"/></svg><div><h3>Manutenção centrada em confiabilidade</h3><p>Planos de manutenção baseados em risco e criticidade dos ativos.</p></div></div>
      <div class="service"><svg width="14" height="14" viewBox="0 0 24 24"><rect x="5" y="10" width="14" height="11" fill="none" stroke="#fff" stroke-width="2"/><path d="M8 10V7a4 4 0 0 1 8 0v3" fill="none" stroke="#fff" stroke-width="2"/></svg><div><h3>Gestão de inventário</h3><p>Levantamento e cadastro completo dos ativos em campo.</p></div></div>
      <div class="service"><svg width="14" height="14" viewBox="0 0 24 24"><path d="M12 3a6 6 0 0 0-3 11v3h6v-3a6 6 0 0 0-3-11zM9 21h6" fill="none" stroke="#fff" stroke-width="2"/></svg><div><h3>Análise de desempenho</h3><p>Indicadores e relatórios para decisões técnicas mais seguras.</p></div></div>
      <div class="service"><svg width="14" height="14" viewBox="0 0 24 24"><path d="M3 17l5-5 4 4 8-8" fill="none" stroke="#fff" stroke-width="2"/></svg><div><h3>Consultoria regulatória</h3><p>Apoio às exigências da agência reguladora do setor elétrico.</p></div></div>
      <div class="service"><svg width="14" height="14" viewBox="0 0 24 24"><circle cx="12" cy="8" r="4" fill="none" stroke="#fff" stroke-width="2"/><path d="M4 21a8 8 0 0 1 16 0" fill="none" stroke="#fff" stroke-width="2"/></svg><div><h3>Treinamento de equipes</h3><p>Capacitação prática para técnicos e gestores de manutenção.</p></div></div>
      <div class="service"><svg width="14" height="14" viewBox="0 0 24 24"><path d="M4 20V12M10 20V8M16 20V4M22 20H2" fill="none" stroke="#fff" stroke-width="2"/></svg><div><h3>Sistemas de gestão</h3><p>Implantação de softwares para o ciclo de vida dos ativos.</p></div></div>
    </div>
  </section>

  <section class="team">
    <h2 class="section-title"><span class="title-icon"></span>DIRETORIA</h2>
    <div class="team-rule"></div>
    <div class="team-grid">
      <div class="member"><div class="member-photo" role="img" aria-label="Foto de diretor de terno"></div><p class="member-name"><b>Nome Sobrenome</b> – Diretor</p></div>
      <div class="member"><div class="member-photo" role="img" aria-label="Foto de diretor de terno"></div><p class="member-name"><b>Nome Sobrenome</b> – Diretor</p></div>
      <div class="member"><div class="member-photo" role="img" aria-label="Foto de diretor de terno"></div><p class="member-name"><b>Nome Sobrenome</b> – Diretor</p></div>
      <div class="member"><div class="member-photo" role="img" aria-label="Foto de diretor de terno"></div><p class="member-name"><b>Nome Sobrenome</b> – Diretor</p></div>
    </div>
  </section>

  <section class="testimonial">
    <h2 class="section-title"><span class="title-icon"></span>NOSSOS CLIENTES</h2>
    <div class="building" role="img" aria-label="Foto de edifício comercial espelhado visto de baixo"></div>
    <div class="quote">
      <div class="quote-mark">“</div>
      <p>But I must explain to you how all this mistaken idea of denouncing pleasure and praising pain was born and I will give you a complete account of the system, and expound the actual teachings of the great.</p>
      <div class="author">
        <div class="author-photo" role="img" aria-label="Foto da cliente"></div>
        <div><div class="author-name">Lúcia Prado</div><div class="author-role">Cargo, Empresa</div></div>
      </div>
    </div>
  </section>

  <section class="clients" aria-label="Empresas clientes">
    <div class="client"></div><div class="client"></div><div class="client"></div><div class="client"></div><div class="client"></div><div class="client"></div>
  </section>

  <footer class="footer">
    <div>
      <h4>Voltra Soluções</h4>
      <p>Gestão de ativos para o setor elétrico com equipe jovem, técnica e comprometida com resultados.</p>
      <h4 style="margin-top:6px">Onde estamos</h4>
      <p>Av. Central, 1000 – Sala 12<br>Centro, São Paulo – SP</p>
    </div>
    <div>
      <div class="contact-row"><svg width="8" height="8" viewBox="0 0 24 24"><path fill="#2b6fc6" d="M6.6 10.8a15 15 0 0 0 6.6 6.6l2.2-2.2c.3-.3.7-.4 1-.2 1.1.4 2.3.6 3.6.6.6 0 1 .4 1 1V20c0 .6-.4 1-1 1A17 17 0 0 1 3 4c0-.6.4-1 1-1h3.5c.6 0 1 .4 1 1 0 1.3.2 2.5.6 3.6.1.3 0 .7-.2 1z"/></svg><div><h4>Fale conosco</h4><p>(11) 4000-1234</p></div></div>
      <div class="contact-row"><svg width="8" height="8" viewBox="0 0 24 24"><rect x="3" y="6" width="18" height="12" fill="none" stroke="#2b6fc6" stroke-width="2"/><path d="M3 6l9 7 9-7" fill="none" stroke="#2b6fc6" stroke-width="2"/></svg><div><h4>Orçamentos</h4><p>contato@voltra.com.br</p></div></div>
      <div class="contact-row"><svg width="8" height="8" viewBox="0 0 24 24"><path fill="#2b6fc6" d="M12 2a7 7 0 0 0-7 7c0 5 7 13 7 13s7-8 7-13a7 7 0 0 0-7-7zm0 9a2 2 0 1 1 0-4 2 2 0 0 1 0 4z"/></svg><div><h4>Atendimento</h4><p>Seg. a sex., 8h às 18h</p></div></div>
    </div>
    <div>
      <div class="field">Nome</div>
      <div class="field">E-mail</div>
      <div class="field tall">Mensagem</div>
      <span class="send">Enviar</span>
    </div>
    <div class="map" role="img" aria-label="Mapa com a localização do escritório"></div>
  </footer>

  <div class="bottom">
    <div class="brand"><span class="brand-dot"></span>Voltra</div>
    <nav class="menu"><span>Página inicial</span><span>Quem somos</span><span>O que fazemos</span><span>Parceiros</span><span>Atendimento</span></nav>
  </div>

</div>
</body>
</html>
```